Design New Business Card, Envelope and Letter Head !

We need a stationery design for our newly developed logo! We need professional classic look.

Front of the Card:
Logo on the left hand side

Personal Detail in the right hand side
i.e. Name,
Title
Office:
Cell:
Fax:
email:

www.ostrellelending.example

Color Scheme should match our logo.

Back Side of the Card:

Logo again with Green back ground or off gray back ground ( Note: Color has to be from logo)

and below message. Again, font size and color should come from logo.

" Manifest your trust in us through the gift of your referrals. We won't let you down."
Updates

Dear Designers;

We have updates few info which we missed earlier. Please include those words in the logo and resubmit your designs for consideration.  We are looking for very professional and classic look. Thanks for your great creation. I have changed the payment options. Please have a look and best of luck.

Tobin

Dear All Designers:

For address; please use following address:

" 4719 Copper Glen Ln, Fenwick Hollow, CA 95017 " 
Please do not use the address in the website. We would like to give business card with option of calling us is the top priority then email then eFax. Please make sure Put " eFax" in the business card. 

Reason: Since I have updated some information per requirements, I would like to give enough time for the great design work.

Just a note to all designers:

"Equal Opportunity Lender" Sign has to be in back  of the card  in a small image. I would say it has to be "inconspicuous". Let's put the NMLS # and CalBRE # in front side. Let's organise the information follow very elegant and professional.

Requirements
Must have
• We must need following Words in the business card

CalBRE License #

NMLS #

And the logo of " Equal Housing Lender ". Please see the logo attached.

Please put these words or logo represents above at the right location of the card.

```html
<!DOCTYPE html>
<html lang="en">
<head>
<meta charset="utf-8">
<title>Ostrelle Lending Stationery</title>
<link rel="stylesheet" href="https://fonts.googleapis.com/css2?family=Tinos:wght@400;700&display=swap">
<style>
  :root {
    --bg: #ececec;
    --paper: #ffffff;
    --ink: #3f3f3f;
    --ink-soft: #6b6b6b;
    --charcoal: #4a4a4a;
    --green: #4f9e1c;
    --green-light: #9ecb7c;
    --faint: #e4e4e4;
  }
  * { box-sizing: border-box; margin: 0; padding: 0; }
  html, body { width: 1200px; height: 795px; overflow: hidden; }
  body { background: var(--bg); font-family: "Tinos", serif; color: var(--ink); position: relative; }

  .piece { position: absolute; background: var(--paper); box-shadow: 0 2px 6px rgba(0,0,0,.12); overflow: hidden; }
  .brand { display: flex; align-items: center; gap: 6px; font-family: "Tinos", serif; font-weight: 400; color: var(--ink); white-space: nowrap; }
  .brand-dot { border-radius: 50%; background: var(--green); flex: none; }
  .brand--light { color: #ffffff; }

  .footer-band { position: absolute; left: 0; right: 0; bottom: 0; display: flex; }
  .footer-band .dark { background: var(--charcoal); flex: 3; }
  .footer-band .green { background: var(--green); flex: 1; }

  /* Business card back */
  .card-back { left: 40px; top: 50px; width: 260px; height: 150px; background: var(--charcoal); padding: 36px 22px; }
  .card-back .brand { font-size: 20px; }
  .card-back .brand-dot { width: 12px; height: 12px; }
  .card-message { margin-top: 12px; font-size: 9px; line-height: 1.5; color: #ffffff; }
  .card-message em { font-style: normal; color: var(--green-light); display: block; }
  .eho-badge { position: absolute; right: 10px; bottom: 10px; width: 12px; height: 12px; border: 1px solid #9a9a9a; }

  /* Business card front */
  .card-front { left: 40px; top: 220px; width: 260px; height: 150px; }
  .card-front .brand { position: absolute; left: 14px; top: 44px; font-size: 13px; }
  .card-front .brand-dot { width: 8px; height: 8px; }
  .card-licenses { position: absolute; left: 14px; top: 80px; font-size: 6.5px; line-height: 1.5; color: var(--ink-soft); }
  .card-person { position: absolute; left: 138px; top: 12px; width: 116px; font-size: 6.2px; line-height: 1.45; color: var(--ink-soft); white-space: nowrap; }
  .card-person .name { font-size: 12px; color: var(--ink); }
  .card-person .title { font-size: 7px; margin-bottom: 4px; }
  .card-person .label { color: var(--green); display: inline-block; width: 22px; }
  .card-person .web { color: var(--green); margin-top: 3px; }
  .card-front .footer-band { height: 8px; }
  .card-front .eho-badge { left: 14px; bottom: 16px; right: auto; }

  /* Notebook cover */
  .notebook { left: 40px; top: 400px; width: 260px; height: 340px; background: var(--charcoal); padding: 130px 30px 0; }
  .notebook .brand { font-size: 24px; }
  .notebook .brand-dot { width: 14px; height: 14px; }
  .notebook .card-message { font-size: 10px; margin-top: 14px; }

  /* Letterhead */
  .letterhead { left: 340px; top: 30px; width: 420px; height: 594px; padding: 36px 40px; }
  .letterhead .brand { font-size: 22px; }
  .letterhead .brand-dot { width: 13px; height: 13px; }
  .lh-contact { position: absolute; right: 40px; top: 34px; font-size: 6.5px; line-height: 1.6; color: var(--ink-soft); }
  .lh-contact .label { color: var(--green); display: inline-block; width: 24px; }
  .lh-watermark { position: absolute; right: -40px; top: 220px; width: 220px; height: 220px; border-radius: 50%; background: var(--faint); }
  .lh-body { position: relative; margin-top: 48px; width: 290px; font-size: 7.5px; line-height: 1.55; color: var(--ink-soft); }
  .lh-body .salutation { font-weight: 700; color: var(--ink); margin-bottom: 8px; }
  .lh-body p { margin-bottom: 8px; }
  .signature { width: 80px; height: 26px; background: linear-gradient(90deg, #d6d6d6, #eeeeee); margin-top: 10px; }
  .signer { font-size: 7px; font-weight: 700; color: var(--ink); margin-top: 3px; }
  .lh-footer { position: absolute; left: 40px; right: 40px; bottom: 22px; font-size: 6px; color: var(--ink-soft); display: flex; align-items: center; gap: 5px; white-space: nowrap; }
  .lh-footer .web { color: var(--green); }
  .lh-footer .eho-badge { position: static; margin-left: auto; flex: none; }
  .letterhead .footer-band { height: 8px; }

  /* Envelope */
  .envelope { left: 790px; top: 60px; width: 370px; height: 176px; padding: 22px 24px; }
  .envelope .brand { font-size: 17px; }
  .envelope .brand-dot { width: 10px; height: 10px; }
  .env-return { margin-top: 6px; font-size: 6.5px; color: var(--ink-soft); }
  .env-return .web { color: var(--green); }
  .env-watermark { position: absolute; right: 24px; top: 16px; width: 90px; height: 90px; border-radius: 50%; background: var(--faint); }
  .envelope .footer-band { height: 8px; }
</style>
</head>
<body>

<section class="piece card-back" aria-label="Business card back">
  <div class="brand brand--light"><span class="brand-dot"></span>Ostrelle Lending</div>
  <p class="card-message">Every referral you share is a vote of confidence.<em>We will honor each one.</em></p>
  <span class="eho-badge"></span>
</section>

<section class="piece card-front" aria-label="Business card front">
  <div class="brand"><span class="brand-dot"></span>Ostrelle Lending</div>
  <div class="card-licenses">CalBRE License # 01234567<br>NMLS # 123456</div>
  <span class="eho-badge"></span>
  <div class="card-person">
    <div class="name">Dana Whitfield</div>
    <div class="title">Mortgage Advisor</div>
    <div><span class="label">Office</span>(925) 555-0142</div>
    <div><span class="label">Cell</span>(925) 555-0187</div>
    <div><span class="label">eFax</span>(925) 555-0199</div>
    <div><span class="label">Email</span>dana@ostrellelending.example</div>
    <div>4719 Copper Glen Ln,<br>Fenwick Hollow, CA 95017</div>
    <div class="web">www.ostrellelending.example</div>
  </div>
  <div class="footer-band"><span class="dark"></span><span class="green"></span></div>
</section>

<section class="piece notebook" aria-label="Notebook cover">
  <div class="brand brand--light"><span class="brand-dot"></span>Ostrelle Lending</div>
  <p class="card-message">Every referral you share is a vote of confidence.<em>We will honor each one.</em></p>
</section>

<section class="piece letterhead" aria-label="Letterhead">
  <div class="lh-watermark"></div>
  <div class="brand"><span class="brand-dot"></span>Ostrelle Lending</div>
  <div class="lh-contact">
    <div><span class="label">Office</span>(925) 555-0142</div>
    <div><span class="label">Fax</span>(925) 555-0199</div>
    <div><span class="label">Email</span>hello@ostrellelending.example</div>
  </div>
  <div class="lh-body">
    <p class="salutation">Lorem Ipsum,</p>
    <p>Sed vitae lorem quis nunc posuere fermentum. Donec at arcu a massa tincidunt aliquet nec eget justo. Nulla facilisi. Integer sit amet velit ut mauris faucibus tempus.</p>
    <p>Vivamus in sem nec purus sodales dignissim. Fusce vel risus ac nibh cursus laoreet, id feugiat ipsum commodo.</p>
    <p>Donec id elit non mi porta gravida at eget metus. Curabitur blandit tempus porttitor, nullam quis risus eget urna mollis ornare vel eu leo.</p>
    <p>Cum sociis natoque penatibus et magnis dis parturient montes. Aenean lacinia bibendum nulla sed consectetur.</p>
    <p>Cras justo odio, dapibus ac facilisis in, egestas eget quam. Maecenas faucibus mollis interdum.</p>
    <div class="signature" role="img" aria-label="Handwritten signature"></div>
    <div class="signer">Company Director</div>
  </div>
  <div class="lh-footer">
    <span>4719 Copper Glen Ln, Fenwick Hollow, CA 95017</span>
    <span>|</span>
    <span class="web">www.ostrellelending.example</span>
    <span>|</span>
    <span>NMLS # 123456</span>
    <span class="eho-badge"></span>
  </div>
  <div class="footer-band"><span class="dark"></span><span class="green"></span></div>
</section>

<section class="piece envelope" aria-label="Envelope">
  <div class="env-watermark"></div>
  <div class="brand"><span class="brand-dot"></span>Ostrelle Lending</div>
  <p class="env-return">4719 Copper Glen Ln, Fenwick Hollow, CA 95017 | <span class="web">www.ostrellelending.example</span></p>
  <div class="footer-band"><span class="dark"></span><span class="green"></span></div>
</section>

</body>
</html>
```